Migration and redesign of existing website to WordPress using DIVI 3

I. TASK OBJECTIVE:
- Redesign our existing website www.harlowsteppodiatry.com.au with a fresh new look and migrate to new Wordpress site based on DIVI3 theme. The site will contain the same basic functionality as the existing site (with some small changes).

II. STYLE/ DESIGN ASPECT:
As an example of a site that I like the look of, see https://quillmarsh.com/. I like the use of shadows, and this would go well with the little animations you can do with Divi (e.g. when hovering over pics).

1. What I am looking for is a design which has lots of white space, is modern and friendly looking (but still not too cute or frivolous, as we are a medical practice)
2. DESIGN that is NOT TOO rectangular or blocky.
3. Please take into consideration our Users are Older market, so any icons or navigation features need to be very easy to understand and not too small.
4. Must be easy to navigate
5. We are are happy to go with a new colour scheme, and are working on some ideas for this, but happy to take suggestions.

III. SPECIFICATIONS:
1. 5+ Pages (should flow like the current site)
2. Using Wordpress Divi 3 theme.
3. I'd like every page to have a "book now" button and a contact form in a sidebar so that users can click the button or fill in the contact form without scrolling at all. EXCEPT ON THE HOME PAGE, where there should still be a book now button (maybe on the top right in the header of all pages?), and maybe a contact us button which scrolls down to the contact area at the bottom of the HOME page. I don't think a side bar is necessarily required on the home page, but if you think it makes sense from a design perspective please let me know.
4. AT THE BOTTOM OF THE PAGE, just above the FOOTER, I'd like a row of trust logos for various organisations that we are affiliated with. (A list of this company will be provided later but you could temporarily use placeholders)

Once we have a structure in place, we can migrate most of the content. Please let me know if I'm not being clear or you need further information.

Podiatry Customers and Referrors

Health Care

Coded - Design and coding required

5+ page

Designer to choose colors to be used in the design.

• Simple to navigate.
• Contact/booking details on most if not all pages - please see specification above
• Section for Trusted Affiliates above the footer
• Wordpress using Divi3 Theme
• Not too busy with the design. Plenty of white space or light background.
• Should not be complicated to navigate.
• TOO rectangular or blocky designs

```html
<!DOCTYPE html>
<html lang="en">
<head>
<meta charset="utf-8">
<title>Harlow Step Podiatry — Home</title>
<link rel="stylesheet" href="https://fonts.googleapis.com/css2?family=Open+Sans:wght@300;400;600;700&display=swap">
<style>
:root{
  --pink:#e8137f;
  --pink-dark:#c90d6c;
  --ink:#333333;
  --text:#666666;
  --muted:#8a8a8a;
  --line:#e2e2e2;
  --beige:#f8f5ef;
  --card:#f2f2f2;
  --tab:#7a7a7a;
  --dark:#3f3f3f;
  --darker:#2c2c2c;
  --badge:#dcdcdc;
  --white:#ffffff;
}
*{box-sizing:border-box;margin:0;padding:0}
html,body{width:1200px;height:4167px;overflow:hidden}
body{font-family:"Open Sans",Arial,sans-serif;color:var(--text);background:var(--white);font-size:13px;line-height:1.6}
a{color:inherit;text-decoration:none}
.wrap{width:900px;margin:0 auto;position:relative}
.btn{display:inline-block;background:var(--pink);color:var(--white);border-radius:30px;font-weight:600;font-size:15px;padding:9px 26px;line-height:1.2;box-shadow:0 4px 10px rgba(232,19,127,.3)}
.center{text-align:center}
.section-title{font-size:32px;font-weight:400;color:var(--ink);text-align:center;line-height:1.2}
.section-title b{font-weight:700}

/* top bar */
.topbar{height:28px;background:var(--pink);color:var(--white);font-size:11px}
.topbar .wrap{display:flex;align-items:center;height:28px;gap:14px}
.topbar .social{display:flex;gap:8px}
.topbar .social span{width:9px;height:9px;border-radius:50%;background:rgba(255,255,255,.85)}
.topbar .right{margin-left:auto;display:flex;gap:18px;font-weight:600}

/* nav */
.nav{height:50px;background:var(--white);box-shadow:0 1px 4px rgba(0,0,0,.08);position:relative;z-index:2}
.nav .wrap{display:flex;align-items:center;height:50px}
.brand{display:flex;align-items:center;gap:7px;font-size:12px;font-weight:600;color:var(--pink)}
.brand i{width:12px;height:12px;border-radius:50%;background:var(--pink);display:block}
.menu{margin-left:auto;display:flex;gap:20px;font-size:12.5px;color:var(--ink);align-items:center;white-space:nowrap}
.menu .active{color:var(--pink);font-weight:600}
.menu svg{display:block}
.menu .book{background:var(--pink);color:var(--white);border-radius:20px;font-weight:600;font-size:12px;padding:5px 14px;line-height:1.2}

/* hero */
.hero{height:339px;position:relative;background:linear-gradient(100deg,#eef0f1 0%,#e7e6e4 55%,#d9cfc8 80%,#ebe8e6 100%)}
.hero .wrap{padding-top:66px}
.hero h1{font-size:50px;font-weight:400;color:var(--ink);line-height:1.1}
.hero h2{font-size:28px;font-weight:700;color:var(--pink);line-height:1.3;margin-top:4px}
.hero .btn{margin-top:26px}
.dots{position:absolute;bottom:14px;left:0;right:0;display:flex;justify-content:center;gap:8px}
.dots span{width:7px;height:7px;border-radius:50%;background:#bbb}
.dots span:first-child{background:var(--ink)}

/* practice areas */
.practice{height:625px;padding-top:88px}
.tabs{display:flex;margin-top:52px}
.tabs span{background:var(--tab);color:var(--white);font-size:13px;font-weight:600;padding:5px 0;text-align:center;border-right:1px solid #fff}
.tabs .on{background:var(--pink)}
.tab-panel{border:1px solid var(--line);padding:18px 22px;height:272px;font-size:12.5px;line-height:1.75}
.tab-panel .links{color:var(--pink);margin-top:10px}
.practice .btn{margin-top:46px}

/* beige info */
.info{height:764px;background:var(--beige);padding-top:64px}
.info h3{font-size:24px;font-weight:400;color:var(--ink);line-height:1.3}
.info h3 em,.caring h3 em{font-style:normal;color:var(--pink)}
.info p,.caring p{font-size:12px;line-height:1.7;margin-top:8px}
.info h3.sub{margin-top:32px}
.info h4{font-size:17px;font-weight:400;color:var(--ink);margin-top:30px}
.conditions{display:flex;justify-content:space-between;margin-top:46px;text-align:center}
.conditions div{width:200px}
.conditions svg{display:block;margin:0 auto 14px}
.conditions span{font-size:14px;color:var(--ink)}

/* caring */
.caring{height:500px;padding-top:66px}
.caring h3{font-size:24px;font-weight:400;color:var(--ink)}
.caring ul{list-style:none;margin-top:10px}
.caring li{font-size:12px;line-height:1.7;padding-left:16px;position:relative;margin-bottom:6px}
.caring li::before{content:"";position:absolute;left:2px;top:8px;width:5px;height:5px;border-radius:50%;background:var(--ink)}
.caring li b{color:var(--ink)}

/* team */
.team{height:791px;padding-top:80px}
.team-grid{display:grid;grid-template-columns:419px 419px;gap:12px 62px;margin-top:44px}
.member{background:var(--card);height:205px;padding:22px 20px;display:flex;gap:18px;box-shadow:0 2px 8px rgba(0,0,0,.06)}
.member:nth-child(n+3){height:236px}
.photo{width:82px;height:96px;flex:none;border-radius:4px;background:linear-gradient(180deg,#dfe3e6,#c9cfd3)}
.member p{font-size:12px;line-height:1.6}
.member .name{color:var(--ink);font-weight:700;margin-top:10px}
.member .role{font-size:11.5px}
.member .role a{color:var(--pink)}
.team .btn{margin-top:50px}

/* cases */
.cases{height:486px;position:relative;background:linear-gradient(115deg,#f4efea 0%,#e9dfd6 40%,#f6f2ee 70%,#ece4dc 100%)}
.cases .wrap{padding-top:72px}
.case-row{display:flex;justify-content:space-between;margin-top:36px}
.case{width:268px;height:261px;background:var(--pink);color:var(--white);text-align:center;padding:26px 24px;border:4px solid rgba(255,255,255,.55);box-shadow:0 6px 16px rgba(0,0,0,.15)}
.case h4{font-size:19px;font-weight:400}
.case p{font-size:12.5px;line-height:1.6;margin-top:10px}
.case .more{display:inline-block;margin-top:18px;border:2px solid var(--white);border-radius:30px;padding:7px 22px;font-size:15px;font-weight:600}

/* contact */
.contact{height:446px;background:var(--dark);color:var(--white)}
.contact .wrap{padding-top:50px}
.contact .section-title{color:var(--white);font-weight:700}
.contact-grid{display:flex;justify-content:space-between;margin-top:34px}
.form{width:428px}
.form .lead{font-size:14px;line-height:1.5}
.field{background:var(--white);height:30px;font-size:11px;color:#999;padding:7px 10px;margin-top:8px}
.pair{display:flex;gap:8px}
.pair .field{flex:1}
.field.msg{height:78px}
.submit-row{display:flex;justify-content:flex-end;align-items:center;gap:10px;margin-top:12px;font-size:12px}
.captcha{width:26px;height:26px;background:var(--white)}
.submit-row .btn{font-size:15px;padding:7px 22px}
.office{width:428px;height:278px;border:1px solid #6a6a6a;padding:18px 22px;margin-top:4px}
.office h5{font-size:18px;font-weight:700;padding-bottom:12px;border-bottom:1px solid #6a6a6a}
.office p{font-size:13px;line-height:1.85;margin-top:12px}
.office .links{color:var(--pink)}

/* trusted affiliates */
.affiliates{height:82px;background:var(--white);border-top:1px solid var(--line)}
.affiliates .wrap{display:flex;align-items:center;justify-content:space-between;height:82px}
.affiliates .label{font-size:13px;font-weight:600;color:var(--ink)}
.affiliates .badges{display:flex;gap:28px}
.affiliates .badges span{width:110px;height:40px;border-radius:6px;background:var(--badge)}

/* footer */
.footer{height:56px;background:var(--darker);color:#9a9a9a;font-size:11px}
.footer .wrap{display:flex;align-items:center;height:56px}
.footer .social{margin-left:auto;display:flex;gap:14px}
.footer .social span{width:12px;height:12px;border-radius:50%;background:#9a9a9a}
</style>
</head>
<body>

<header>
  <div class="topbar">
    <div class="wrap">
      <span>(08) 5550 2148</span>
      <div class="social"><span></span><span></span><span></span><span></span></div>
      <div class="right"><a href="#">Blog</a><a href="#">Contact</a></div>
    </div>
  </div>
  <nav class="nav">
    <div class="wrap">
      <a class="brand" href="#"><i></i>Harlow Step Podiatry</a>
      <div class="menu">
        <a class="active" href="#">Home</a>
        <a href="#">Common Problems ▾</a>
        <a href="#">Services</a>
        <a href="#">About Us</a>
        <a href="#">Case Histories</a>
        <a href="#">Helpful Information ▾</a>
        <svg width="13" height="13" viewBox="0 0 13 13" aria-label="Search"><circle cx="5.5" cy="5.5" r="4.3" fill="none" stroke="#555" stroke-width="1.5"/><line x1="8.6" y1="8.6" x2="12" y2="12" stroke="#555" stroke-width="1.6"/></svg>
        <a class="book" href="#">Book now</a>
      </div>
    </div>
  </nav>
</header>

<section class="hero" role="img" aria-label="Soft photo of bare feet resting on a light floor">
  <div class="wrap">
    <h1>We offer solutions</h1>
    <h2>to common foot problems</h2>
    <a class="btn" href="#">Book now</a>
  </div>
  <div class="dots"><span></span><span></span><span></span></div>
</section>

<section class="practice">
  <div class="wrap">
    <h2 class="section-title"><b>Practice</b> Areas</h2>
    <div class="tabs">
      <span class="on" style="width:194px">Common Problems</span>
      <span style="width:225px">Foot and Ankle Surgery</span>
      <span style="width:167px">Sports and Dance</span>
      <span style="width:158px">All Our Services</span>
    </div>
    <div class="tab-panel">
      <p>When you suffer from a foot and/or ankle problem, the pain and discomfort can make it a challenge to engage in simple, daily activities. When the pain disrupts your life, you need to contact a skilled, experienced podiatrist to get resolution. The podiatrists at Harlow Step Podiatry offer a variety of treatment options for many common foot and ankle conditions, including Achilles tendon injuries, ankle sprains, flat foot and clavus foot, and bunions and ingrown toenails. Their primary concern is the health of their patients' feet and ankles, and they use advanced equipment and work with other professionals, including trainers and physical therapists, to ensure a successful outcome. To discuss your foot and ankle pain, contact our Wrenfield office at <b>08 5550 2148</b>.</p>
      <p class="links">Achilles Tendon Injuries / Ankle Sprains / Bunions / Corns and callouses / Heel and Arch Pain / High Arch Foot (Pes Cavus) / Ingrown Toenails / Fungal Nails / Flatfeet / Skin and Nail Care / Stiff Big Toe (Hallux Rigidus)</p>
    </div>
    <div class="center"><a class="btn" href="#">View All</a></div>
  </div>
</section>

<section class="info">
  <div class="wrap">
    <h3><em>Let Our</em> Wrenfield Podiatrists Relieve Your Foot and Ankle Pain</h3>
    <p>Whether you are an office worker, pensioner, or professional athlete, nearly all people will experience problems in their feet and ankles at some point in their lives. Unfortunately, a problem in the foot can affect the whole body, causing an infection to spread, deformities in the foot, and pain to travel upward into the leg.</p>
    <p>It doesn't take long before a foot injury may cause wide-ranging consequences, including lost mobility, a drain on your finances, and a decline in your physical health. Even when patients attempt to cure their conditions once and for all, they often suffer the frustration of treating the symptoms of their condition only to have the problem return in full force.</p>
    <h3 class="sub"><em>A Proven</em> Track Record of Correcting Foot Pain in Calder Bay Patients</h3>
    <p>At Harlow Step Podiatry, we know that there are often a variety of causes of foot and ankle pain, and each must be addressed to solve your problem for good. We examine your feet, posture, and gait to identify any biomechanical issues that could be causing your pain, treat ulcerations and foot deformities that prohibit full range of motion, and perform many different surgical techniques to restore your mobility and lifestyle. Call the number on this page today to tell our podiatrists about your condition and schedule your appointment.</p>
    <p>Our Calder Bay clinic has provided comprehensive podiatry care to all age groups across the region since 1981. Since our practice was established, our success has allowed us to grow and expand our services, currently hosting six on-staff podiatrists and a variety of the most advanced techniques and equipment to treat foot and ankle pain. In our Wrenfield offices, we can advise you on many matters relating to your feet and legs, including footwear, skin care, walking difficulties, and sports injuries. We stay up to date with the latest methods in podiatry and foot care treatment options, and can give you the intervention and information you need to relieve your condition for good.</p>
    <p>It is our goal to give each of our patients personalized care and recovery options to meet their specific needs. Whether you want to stop a recurring condition from coming back, restore lost function, or optimize the mobility you have, we can advise you on the best way to accomplish your goals.</p>
    <h4>We treat a wide range of conditions, including:</h4>
    <div class="conditions">
      <div>
        <svg width="46" height="46" viewBox="0 0 46 46" role="img" aria-label="Heel icon"><rect x="8" y="4" width="30" height="38" rx="14" fill="none" stroke="#e8137f" stroke-width="2.5"/><circle cx="23" cy="30" r="5" fill="#e8137f"/></svg>
        <span>Heel and Arch Pain</span>
      </div>
      <div>
        <svg width="46" height="46" viewBox="0 0 46 46" role="img" aria-label="Running shoe icon"><path d="M5 32 L14 14 L22 20 L30 24 L41 28 L41 36 L5 36 Z" fill="none" stroke="#e8137f" stroke-width="2.5" stroke-linejoin="round"/></svg>
        <span>Sports Injuries</span>
      </div>
      <div>
        <svg width="46" height="46" viewBox="0 0 46 46" role="img" aria-label="Nail care icon"><rect x="12" y="6" width="22" height="34" rx="10" fill="none" stroke="#e8137f" stroke-width="2.5"/><rect x="17" y="10" width="12" height="9" rx="4" fill="#e8137f"/></svg>
        <span>Skin and Nail Care</span>
      </div>
      <div>
        <svg width="46" height="46" viewBox="0 0 46 46" role="img" aria-label="Foot outline icon"><path d="M16 4 H30 V28 Q34 40 22 42 Q10 42 14 30 Z" fill="none" stroke="#e8137f" stroke-width="2.5" stroke-linejoin="round"/></svg>
        <span>Foot and Ankle Surgery</span>
      </div>
    </div>
  </div>
</section>

<section class="caring">
  <div class="wrap">
    <h3><em>Caring</em> for Patients From All Walks of Life</h3>
    <p>We know it can be difficult to seek treatment for a condition, especially if the way forward could mean surgery or a lengthy recovery. That is why we use every advantage to ease our customers' minds as well as their discomfort. In our office, we help our patients:</p>
    <ul>
      <li><b>Regain control:</b> Just like you, we want you to get better as soon as possible. That is why we focus on making your visit an informative and supportive experience, empowering you to take control of your condition and make the best possible treatment choice. We even offer specific solutions to athletes, such as ballet dancers, football players, and others suffering from sporting injuries.</li>
      <li><b>Explore all possible solutions:</b> We offer both non-invasive and surgical remedies for most conditions, and have a medical team in office for musculoskeletal treatments. We often work with trainers, physical therapists, and other professionals to provide additional intervention and rehabilitation options. Our foot surgeries range from minor in-house procedures (such as ingrown toenails and wart removal) to off-site surgeries for bunions, toe deformities, and advanced reconstructive foot surgery.</li>
      <li><b>Stay pain-free for life:</b> We build relationships with our patients, keeping them on their feet for as long as they live. Since we remove neuromas, correct sporting injuries, create customized insoles (orthoses) to correct gait and posture, and offer preventive and corrective wound care for adults, we are a one-stop shop for comprehensive foot care for the whole family.</li>
    </ul>
    <p>We combine our state-of-the-art equipment and medical experience with our competent, friendly staff, making it as easy as possible for our patients to get relief. It is our goal for you to walk away with your problems addressed, but also having had a great experience at the same time. Call the number on this page or fill out our online contact form to make an appointment today.</p>
  </div>
</section>

<section class="team">
  <div class="wrap">
    <h2 class="section-title"><b>Meet</b> Our Team</h2>
    <div class="team-grid">
      <article class="member">
        <div class="photo" role="img" aria-label="Portrait of Dana Whitlock"></div>
        <div>
          <p>Dana is the practice principal and founded the practice over 25 years ago. She is a Podiatric Surgeon and nowadays focuses exclusively on surgical treatment of the foot. Examples of the problems she treats surgically include bunions, hammer toes and other toe deformities...</p>
          <p class="name">Dana Whitlock</p>
          <p class="role">Podiatric Surgeon, <a href="#">Harlow Step Podiatry</a></p>
        </div>
      </article>
      <article class="member">
        <div class="photo" role="img" aria-label="Portrait of Marcus Pell"></div>
        <div>
          <p>After spending several years working as a software engineer, Marcus went back to study in 1996. He graduated with a Bachelor of Science in Podiatry with First Class Honours in 1998, obtained a Post Graduate Diploma in Podiatry in 2000, and a Master's Degree in Podiatry in 2004.</p>
          <p class="name">Marcus Pell</p>
          <p class="role">Podiatrist, <a href="#">Harlow Step Podiatry</a></p>
        </div>
      </article>
      <article class="member">
        <div class="photo" role="img" aria-label="Portrait of Tessa Rowan"></div>
        <div>
          <p>Tessa first attended Harlow Step Podiatry as a patient in 2005, which sparked her interest in health care and podiatry. In Year 10 at school she chose a local podiatry clinic for work experience, where she loved adjusting orthotics and meeting new people. Tessa went on to complete a four year Bachelor of Podiatric Medicine at WCU and has been working full...</p>
          <p class="name">Tessa Rowan</p>
          <p class="role">Podiatrist, <a href="#">Harlow Step Podiatry</a></p>
        </div>
      </article>
      <article class="member">
        <div class="photo" role="img" aria-label="Portrait of Nina Castell"></div>
        <div>
          <p>Nina's interest in podiatry stems from her keen interest in long-distance running and loves all sports and the outdoors. Seeing a podiatrist due to biomechanical issues when she was at school piqued her interest and helped her realise how important feet are in everyday life. This experience led her to study a Bachelor of Science (Podiatry) at Westhaven University.</p>
          <p class="name">Nina Castell</p>
          <p class="role">Podiatrist, <a href="#">Harlow Step Podiatry</a></p>
        </div>
      </article>
    </div>
    <div class="center"><a class="btn" href="#">View All Members</a></div>
  </div>
</section>

<section class="cases" aria-label="Case histories">
  <div class="wrap">
    <h2 class="section-title"><b>Case</b> Histories</h2>
    <div class="case-row">
      <article class="case">
        <h4>Plantar fascia Case</h4>
        <p>The case histories and outcomes presented here are for general information only and do not replace the advice of a health professional. You should always consult...</p>
        <a class="more" href="#">Read More</a>
      </article>
      <article class="case">
        <h4>Bunion Case</h4>
        <p>The case histories and outcomes presented here are for general information only and do not replace the advice of a health professional. You should always consult...</p>
        <a class="more" href="#">Read More</a>
      </article>
      <article class="case">
        <h4>Trauma case</h4>
        <p>The case histories and outcomes presented here are for general information only and do not replace the advice of a health professional. You should always consult...</p>
        <a class="more" href="#">Read More</a>
      </article>
    </div>
  </div>
</section>

<section class="contact" id="contact">
  <div class="wrap">
    <h2 class="section-title">Contact Us</h2>
    <div class="contact-grid">
      <form class="form">
        <p class="lead">Please fill out this quick contact form and someone will be in touch with you shortly!</p>
        <div class="field">Name</div>
        <div class="pair"><div class="field">Email Address</div><div class="field">Phone Number</div></div>
        <div class="field msg">Message</div>
        <div class="submit-row"><span>4 + 2 =</span><span class="captcha"></span><span class="btn">Submit</span></div>
      </form>
      <div class="office">
        <h5>Wrenfield Office</h5>
        <p>14 Larkspur Lane<br>Wrenfield, WA 6999<br>Phone: (08) 5550 2148<br><span class="links">Contact Details | Get Directions</span></p>
      </div>
    </div>
  </div>
</section>

<section class="affiliates" aria-label="Trusted affiliates">
  <div class="wrap">
    <span class="label">Trusted Affiliates</span>
    <div class="badges">
      <span role="img" aria-label="Affiliate badge"></span>
      <span role="img" aria-label="Affiliate badge"></span>
      <span role="img" aria-label="Affiliate badge"></span>
      <span role="img" aria-label="Affiliate badge"></span>
      <span role="img" aria-label="Affiliate badge"></span>
    </div>
  </div>
</section>

<footer class="footer">
  <div class="wrap">
    <span>©2017 Harlow Step Podiatry. All Rights Reserved. Reproduced with Permission. Privacy Policy</span>
    <div class="social"><span></span><span></span><span></span><span></span></div>
  </div>
</footer>

</body>
</html>
```